K3 Construction Site Sign

I would like to get a sign designed which would be installed at a construction sign. I would like to incorporate my current logo, font and colors in the sign. The sign would be 30" x 60" (vertical). Would like to keep it clean and simple yet eye catching and sparks interest. I have attached my branding colors. I would like the background to be the branded blue with white text.

```html
<!DOCTYPE html>
<html lang="en">
<head>
<meta charset="utf-8">
<title>K3 Construction Site Sign</title>
<link rel="stylesheet" href="https://fonts.googleapis.com/css2?family=Montserrat:wght@400;600&display=swap">
<style>
  :root {
    --brand-blue: #285282;
    --brand-blue-light: #2f5e91;
    --brand-yellow: #f9ae40;
    --text-white: #ffffff;
    --page-bg: #ffffff;
  }
  html, body {
    margin: 0;
    padding: 0;
    width: 1200px;
    height: 829px;
    overflow: hidden;
    background: var(--page-bg);
  }
  .canvas {
    position: relative;
    width: 1200px;
    height: 829px;
  }
  .site-sign {
    position: absolute;
    left: 420px;
    top: 54px;
    width: 360px;
    height: 720px;
    box-shadow: 2px 3px 6px rgba(0, 0, 0, 0.25);
  }
  .sign-bg { fill: var(--brand-blue); }
  .accent-corner { fill: var(--brand-yellow); }
  .watermark-name {
    fill: var(--brand-blue-light);
    font-family: "Montserrat", sans-serif;
    font-weight: 600;
  }
  .brand-name {
    fill: var(--text-white);
    font-family: "Montserrat", sans-serif;
    font-weight: 600;
  }
  .company-line {
    fill: var(--text-white);
    font-family: "Montserrat", sans-serif;
    font-weight: 400;
  }
</style>
</head>
<body>
<main class="canvas">
  <svg class="site-sign" viewBox="0 0 577 1155" xmlns="http://www.w3.org/2000/svg" aria-label="K3 Construction &amp; Renovations Ltd. site sign">
    <defs>
      <clipPath id="sign-area">
        <rect width="577" height="1155"/>
      </clipPath>
    </defs>
    <g clip-path="url(#sign-area)">
      <rect class="sign-bg" width="577" height="1155"/>
      <text class="watermark-name" font-size="360" textLength="500" lengthAdjust="spacingAndGlyphs"
            transform="translate(600,740) rotate(-90)">K3</text>
      <polygon class="accent-corner" points="0,822 0,1155 333,1155"/>
      <text class="brand-name" font-size="190" textLength="140" lengthAdjust="spacingAndGlyphs"
            transform="translate(276,875) rotate(-90)">K3</text>
      <text class="company-line" font-size="72" textLength="545" lengthAdjust="spacingAndGlyphs"
            transform="translate(195,712) rotate(-90)">CONSTRUCTION &amp;</text>
      <text class="company-line" font-size="72" textLength="640" lengthAdjust="spacingAndGlyphs"
            transform="translate(275,712) rotate(-90)">RENOVATIONS LTD.</text>
    </g>
  </svg>
</main>
</body>
</html>
```